Education related business need name card design

We need name card design for long term study agent.
Company name is Harbor Lantern.
We support clients to connect to the world.
Clients are Japanese family who has primary and secondary school students.

Company Logo is reflection of the globe and HL (Harbor Lantern).
Since business is related to education, we would like to show reliability and love to see the world map (atlas) in the name card.

Target Market(s)

late 30's to 50's parents of primary and secondary students who are enthusiastic for education. Secondary school management

Industry/Entity Type

Education

Contact Information for Business Card

Company name, Address, Official position, Name, Phone number, Mobile number, email address,

Font styles to use
Serif
Other font styles liked:
• Century Gothic(logo)

Requirements
Must have
• Since businee is related to education, we would like to show reliability and love to see the world map (atlas) in the name card.

```html
<!DOCTYPE html>
<html lang="en">
<head>
<meta charset="utf-8">
<title>Harbor Lantern – Business Card</title>
<link href="https://fonts.googleapis.com/css2?family=Lato:wght@400;700;900&display=swap" rel="stylesheet">
<style>
  :root {
    --stage: #e6e7ea;
    --card-back: #e4e5e7;
    --card-white: #ffffff;
    --brand-blue: #2b5c9c;
    --brand-blue-dark: #1f4a85;
    --brand-blue-light: #3a6fb3;
    --map-grey: #eceef1;
    --ink: #333a44;
    --ink-soft: #5a626d;
  }
  * { box-sizing: border-box; margin: 0; padding: 0; }
  html, body { width: 1200px; height: 800px; overflow: hidden; }
  body {
    background: var(--stage);
    font-family: 'Lato', sans-serif;
    position: relative;
  }
  .card {
    position: absolute;
    top: 245px;
    width: 540px;
    height: 310px;
    border-radius: 4px;
    overflow: hidden;
    box-shadow: 0 6px 18px rgba(0,0,0,0.18);
  }
  /* ---------- back side ---------- */
  .card-back {
    left: 45px;
    background: var(--card-back);
    display: flex;
    align-items: center;
    justify-content: center;
    gap: 16px;
  }
  .brand-mark {
    width: 58px; height: 58px;
    border-radius: 50%;
    background: var(--brand-blue);
    flex: none;
  }
  .brand-name {
    color: var(--brand-blue);
    font-weight: 400;
    font-size: 30px;
    line-height: 1.02;
  }
  /* ---------- front side ---------- */
  .card-front {
    left: 615px;
    background: var(--card-white);
  }
  .atlas-backdrop {
    position: absolute;
    left: 0; top: 100px; right: 0; bottom: 0;
    background: radial-gradient(ellipse at 70% 50%, var(--map-grey), #f7f8fa 70%);
  }
  .header-band {
    position: absolute;
    left: 0; top: 0; right: 0; height: 100px;
    background: linear-gradient(90deg, var(--brand-blue-dark), var(--brand-blue) 60%, var(--brand-blue-light));
  }
  .atlas-panel {
    position: absolute;
    left: 0; top: 0; width: 300px; height: 190px;
    background: radial-gradient(ellipse at 35% 55%, #6f93c4 0%, var(--brand-blue) 55%, var(--brand-blue-dark) 100%);
  }
  .front-logo {
    position: absolute;
    left: 215px; top: 40px;
    display: flex; align-items: center; gap: 7px;
  }
  .front-logo .brand-mark { width: 28px; height: 28px; background: var(--brand-blue-light); }
  .front-logo .brand-name { color: #dbe6f4; font-size: 14px; }
  .person {
    position: absolute;
    right: 22px; top: 32px;
    text-align: right;
    color: #fff;
  }
  .person-name { font-weight: 900; font-size: 20px; letter-spacing: 1px; }
  .person-title { font-size: 12px; margin-top: 2px; color: #dfe7f2; }
  .address {
    position: absolute;
    left: 140px; top: 198px;
    color: var(--ink);
  }
  .address-company {
    font-weight: 900;
    font-size: 13px;
    color: var(--brand-blue);
    border-bottom: 2px solid var(--brand-blue);
    padding-bottom: 2px;
    margin-bottom: 3px;
  }
  .address-line { font-size: 12.5px; line-height: 1.25; }
  .divider {
    position: absolute;
    left: 318px; top: 120px; width: 1px; height: 100px;
    background: #a9b3c1;
  }
  .contacts {
    position: absolute;
    left: 340px; top: 125px;
    list-style: none;
    color: var(--ink-soft);
    font-size: 12.5px;
  }
  .contacts li { display: flex; align-items: center; gap: 8px; height: 24px; }
  .contacts svg { width: 14px; height: 14px; fill: var(--brand-blue); flex: none; }
  .stripe {
    position: absolute;
    left: 0; right: 0;
    background: var(--brand-blue);
  }
  .stripe-main { top: 262px; height: 5px; }
  .stripe-thin { top: 290px; height: 4px; }
</style>
</head>
<body>
  <section class="card card-back" aria-label="Card back">
    <span class="brand-mark"></span>
    <span class="brand-name">Harbor Lantern<br>Pte.Ltd.</span>
  </section>

  <section class="card card-front" aria-label="Card front">
    <div class="atlas-backdrop" role="img" aria-label="Faint grey world map in the background"></div>
    <div class="header-band"></div>
    <div class="atlas-panel" role="img" aria-label="White world map on blue"></div>

    <div class="front-logo">
      <span class="brand-mark"></span>
      <span class="brand-name">Harbor Lantern<br>Pte.Ltd.</span>
    </div>

    <div class="person">
      <div class="person-name">Mark Ellison</div>
      <div class="person-title">Owner &amp; CEO</div>
    </div>

    <div class="address">
      <div class="address-company">Harbor Lantern</div>
      <div class="address-line">48 Riverside 9th Street</div>
      <div class="address-line">Linden, TX 78000</div>
    </div>

    <div class="divider"></div>

    <ul class="contacts">
      <li>
        <svg viewBox="0 0 16 16" aria-hidden="true"><path d="M3 2h3l1 3-2 1a8 8 0 0 0 5 5l1-2 3 1v3c0 1-1 1-1 1C7 14 2 9 2 3c0 0 0-1 1-1z"/></svg>
        <span>512-555-01846</span>
      </li>
      <li>
        <svg viewBox="0 0 16 16" aria-hidden="true"><path d="M1 3h14v10H1z M2 4l6 5 6-5" fill="none" stroke="#2b5c9c" stroke-width="1.4"/></svg>
        <span>mark@harborlantern.com</span>
      </li>
      <li>
        <svg viewBox="0 0 16 16" aria-hidden="true"><g fill="none" stroke="#2b5c9c" stroke-width="1.3"><circle cx="8" cy="8" r="6.5"/><ellipse cx="8" cy="8" rx="3" ry="6.5"/><path d="M1.5 8h13"/></g></svg>
        <span>www.harborlantern.com</span>
      </li>
    </ul>

    <div class="stripe stripe-main"></div>
    <div class="stripe stripe-thin"></div>
  </section>
</body>
</html>
```